Photography Business, Business Card

Looking for a unique cutting edge card that takes advantage of the latest printing technologies. Please review this site for all the options they office: https://plumeprints.example. If you can think it they can do it. And if you have an idea and do not know if they can do it, I will check into it.
Updates

Target Market(s)

People and places I took images of and future clients.

Industry/Entity Type

Photography

Contact Information for Business Card

Name, cell & email. Colin Hartley, chartley@kvnphoto.example, 318-742-9061

Colors

Designer to choose only greyscale colors for use in the design.

Requirements
Must have
• 100% cutting edge. Is so great, those I hand it to always show it to someone else. A piece of art.
Nice to have
• Blacks, silvers, greys, some red. Maybe other colors?

```html
<!DOCTYPE html>
<html lang="en">
<head>
<meta charset="utf-8">
<title>Colin Hartley – Business Card</title>
<link rel="stylesheet" href="https://fonts.googleapis.com/css2?family=Exo+2:wght@700&family=Arimo:wght@400&display=swap">
<style>
  :root {
    --page: #ffffff;
    --card-dark: #2e2e2e;
    --card-light: #e1e2e2;
    --tab-grey: #9a9a9a;
    --accent-red: #e8262b;
    --text-light: #d9d9d9;
    --text-muted: #8c8c8c;
    --logo-dark: #3a3a3a;
    --frame-line: #b9baba;
    --lens-outer: #0b0b0b;
    --lens-mid: #3c3d3f;
    --lens-core: #111112;
  }
  html, body {
    margin: 0;
    padding: 0;
    width: 1200px;
    height: 1200px;
    overflow: hidden;
    background: var(--page);
  }
  .canvas {
    display: block;
    width: 1200px;
    height: 1200px;
  }
  .card-name {
    font-family: "Exo 2", "Arial Black", sans-serif;
    font-weight: 700;
    font-size: 22px;
    fill: var(--accent-red);
    letter-spacing: 0.5px;
  }
  .card-role {
    font-family: "Arimo", Arial, sans-serif;
    font-size: 16px;
    fill: var(--text-light);
  }
  .card-contact {
    font-family: "Arimo", Arial, sans-serif;
    font-size: 18px;
    fill: var(--text-muted);
  }
  .card-contact--email { font-size: 17px; }
  .contact-icon {
    fill: none;
    stroke: var(--text-muted);
    stroke-width: 1.4;
    stroke-linejoin: round;
    stroke-linecap: round;
  }
  .brand-name {
    font-family: "Arimo", Arial, sans-serif;
    font-size: 44px;
    fill: var(--logo-dark);
    letter-spacing: 2px;
  }
  .brand-person {
    font-family: "Arimo", Arial, sans-serif;
    font-size: 30px;
    fill: var(--logo-dark);
  }
</style>
</head>
<body>
<svg class="canvas" viewBox="0 0 1000 1000" xmlns="http://www.w3.org/2000/svg">
  <defs>
    <radialGradient id="lens-gradient" cx="50%" cy="48%" r="50%">
      <stop offset="0%" stop-color="var(--lens-core)"/>
      <stop offset="30%" stop-color="#2a2b2d"/>
      <stop offset="55%" stop-color="var(--lens-mid)"/>
      <stop offset="85%" stop-color="#1e1f20"/>
      <stop offset="100%" stop-color="var(--lens-outer)"/>
    </radialGradient>
  </defs>

  <!-- Front of card -->
  <g class="card-front">
    <path class="card-front__body" fill="var(--card-dark)"
          d="M182,144 A14,14 0 0 1 196,130 H613 A171,171 0 0 1 613,472 H182 Z"/>
    <path class="card-front__tab" fill="var(--tab-grey)"
          d="M220,130 H276 V194 A28,28 0 0 1 220,194 Z"/>

    <circle class="lens-ring" cx="613" cy="301" r="169" fill="var(--lens-outer)"
            stroke="var(--accent-red)" stroke-width="5"/>
    <circle class="lens-artwork" cx="613" cy="301" r="158" fill="url(#lens-gradient)"
            role="img" aria-label="Camera lens illustration"/>

    <text class="card-name" x="208" y="310">Colin Hartley</text>
    <text class="card-role" x="209" y="333">Creative Visual Services</text>

    <path class="contact-icon" d="M212,366 l4,-2 l4,6 l-3,3 q3,6 9,9 l3,-3 l6,4 l-2,4 q-10,2 -18,-7 q-7,-8 -3,-14 z"/>
    <text class="card-contact" x="244" y="383">(318)742-9061</text>

    <rect class="contact-icon" x="208" y="399" width="22" height="15" rx="1"/>
    <polyline class="contact-icon" points="208,400 219,409 230,400"/>
    <text class="card-contact card-contact--email" x="242" y="411">chartley@kvnphoto.example</text>
  </g>

  <!-- Back of card -->
  <g class="card-back">
    <path class="card-back__body" fill="var(--card-light)"
          d="M180,540 A12,12 0 0 1 192,528 H607 A171,171 0 0 1 607,870 H180 Z"/>
    <path class="card-back__frame" fill="none" stroke="var(--frame-line)" stroke-width="1"
          d="M205,560 A12,12 0 0 1 217,549 H607 A150,150 0 0 1 607,849 H205 Z"/>

    <text class="brand-name" x="247" y="716">KVN</text>
    <line class="brand-divider" x1="455" y1="672" x2="455" y2="726" stroke="var(--frame-line)" stroke-width="1"/>
    <text class="brand-person" x="470" y="710">Colin Hartley</text>
  </g>
</svg>
</body>
</html>
```